Cocktail Reception Invitation - For New Office Location

We are a residential property management, investment, and acquisition company and we have recently moved to a new corporate headquarters. We are hosting an event for current customers/vendors, as well as prospects, to show off the new office and enhance the legitimacy of our brand. The event will be a cocktail reception with heavy appetizers/hors d'oeuvres and a bar. We want the invitation to be professional, clean, and somewhat modern. Would be great if we could have it formatted for both electronic delivery AND print, but print is the priority. Thanks in advance for submitting! Photo of the new building attached - does not have to be on the invitation though.

Target Market(s)

Investors, Property Owners, Contractors

Industry/Entity Type

Real Estate

Requirements
Must have
• Must have placeholders for event date, time, location, RSVP, etc. Date is Thursday November 17th from 4-7:00 PM at 418 W Marlow St, Indianapolis, IN 46208. The invitees are a very professional group of people and the invitation should be classy and clean.
Nice to have
• Our colors are Navy Blue, Orange, and dark gray. Not required if it doesn't look good on the invite but it might be nice. I have included a photo of the new office if it makes sens to have it on the invitation.

```html
<!DOCTYPE html>
<html lang="en">
<head>
<meta charset="utf-8">
<title>Cocktail Party Invitation</title>
<link rel="stylesheet" href="https://fonts.googleapis.com/css2?family=Pinyon+Script&family=Source+Sans+3:wght@400;500&display=swap">
<style>
  :root {
    --paper: #b1b1b1;
    --navy: #0707ad;
    --orange: #f38a12;
    --soft-text: #a9abbd;
    --ink: #141414;
    --dot: #7d7d88;
    --frame-dots: #333333;
    --cream: #f4efe2;
    --sprig-light: #e6e2d6;
    --sprig-dark: #3a3a3a;
  }
  html, body {
    margin: 0;
    padding: 0;
    width: 1200px;
    height: 1200px;
    overflow: hidden;
    background: var(--paper);
  }
  .invitation {
    position: relative;
    width: 1200px;
    height: 1200px;
    background: var(--paper);
    font-family: "Source Sans 3", "Myriad Pro", sans-serif;
  }
  .invitation__art {
    position: absolute;
    inset: 0;
  }
  .line {
    position: absolute;
    left: 0;
    width: 1200px;
    text-align: center;
    margin: 0;
    line-height: 1;
    white-space: nowrap;
  }
  .lead {
    color: var(--soft-text);
    font-size: 25px;
    letter-spacing: 0.5px;
  }
  .lead--invited { top: 277px; }
  .lead--office { top: 477px; }
  .event-title {
    top: 342px;
    color: var(--orange);
    font-family: "Pinyon Script", cursive;
    font-size: 84px;
    padding-left: 10px;
  }
  .address {
    color: var(--soft-text);
    font-size: 36px;
    font-variant: small-caps;
  }
  .address--street { top: 548px; }
  .address--city { top: 593px; }
  .when {
    color: var(--orange);
    font-size: 30px;
    font-variant: small-caps;
  }
  .when--date { top: 668px; }
  .when--time { top: 706px; }
  .rsvp-title {
    top: 905px;
    color: var(--navy);
    font-family: "Pinyon Script", cursive;
    font-size: 72px;
    padding-left: 6px;
  }
  .rsvp-contact {
    top: 1013px;
    color: var(--ink);
    font-size: 33px;
    font-variant: small-caps;
  }
</style>
</head>
<body>
<main class="invitation">
  <svg class="invitation__art" width="1200" height="1200" viewBox="0 0 1200 1200" xmlns="http://www.w3.org/2000/svg">
    <defs>
      <radialGradient id="sprig-soft" cx="50%" cy="50%" r="50%">
        <stop offset="0%" stop-color="#d8d5cc" stop-opacity="0.9"/>
        <stop offset="60%" stop-color="#9c9c9c" stop-opacity="0.55"/>
        <stop offset="100%" stop-color="#b1b1b1" stop-opacity="0"/>
      </radialGradient>
      <radialGradient id="sprig-faint" cx="50%" cy="50%" r="50%">
        <stop offset="0%" stop-color="#9a9a9a" stop-opacity="0.55"/>
        <stop offset="100%" stop-color="#b1b1b1" stop-opacity="0"/>
      </radialGradient>
    </defs>

    <!-- frame -->
    <rect class="frame-dotted" x="43" y="41" width="1117" height="1117" fill="none" stroke="var(--frame-dots)" stroke-width="2" stroke-dasharray="2 3"/>
    <rect class="frame-navy" x="61" y="57" width="1080" height="1084" fill="none" stroke="var(--navy)" stroke-width="5"/>
    <rect class="frame-cream" x="69" y="65" width="1064" height="1068" fill="none" stroke="var(--cream)" stroke-width="2"/>

    <!-- floral sprays -->
    <g role="img" aria-label="Spray of small white blossoms and dark berry sprigs, upper left">
      <ellipse cx="285" cy="290" rx="130" ry="125" fill="url(#sprig-soft)"/>
    </g>
    <g role="img" aria-label="Faint grey blossom sprigs, left">
      <ellipse cx="205" cy="560" rx="90" ry="100" fill="url(#sprig-faint)"/>
    </g>
    <g role="img" aria-label="Faint grey blossom sprigs, right">
      <ellipse cx="975" cy="480" rx="55" ry="75" fill="url(#sprig-faint)"/>
    </g>
    <g role="img" aria-label="Spray of small white blossoms and dark berry sprigs, lower right">
      <ellipse cx="940" cy="720" rx="140" ry="130" fill="url(#sprig-soft)"/>
    </g>

    <!-- medallion -->
    <circle class="medallion" cx="600" cy="505" r="357" fill="var(--navy)"/>
    <circle class="medallion-dots" cx="600" cy="505" r="331" fill="none" stroke="var(--dot)" stroke-width="9" stroke-linecap="round" stroke-dasharray="0 20.8"/>
  </svg>

  <p class="line lead lead--invited">YOU ARE INVITED TO A</p>
  <h1 class="line event-title" style="font-weight:400">Cocktail Party</h1>
  <p class="line lead lead--office">AT OUR NEW OFFICE AT</p>
  <p class="line address address--street">418 W Marlow St,</p>
  <p class="line address address--city">Indianapolis, IN 46208</p>
  <p class="line when when--date">Thursday | November 17, 2016</p>
  <p class="line when when--time">4:00 PM to 7:00 PM</p>
  <p class="line rsvp-title">Rsvp</p>
  <p class="line rsvp-contact">to Clara Finch | 0123.555.0148</p>
</main>
</body>
</html>
```